Vindhalur - Start-up company selling electricity

Hello let me tell you about Vindhalur.

Vindhalur is start-up company selling electricity in Iceland. The operations of the company consist of making power usage forecasts for our customers, purchasing the electricity wholesale from the energy producers, and selling the electricity to the consumer. We are focused on tech by using optimization and machine learning to minimize electricity prices to our customers. Our marketing strategy is to portray a tech company mindset and to show dedication to driving down the electricity price on the market.

We need your help to make our website pop. Possible concepts to work with are as follows:

- Iceland the land of ice and fire
- Green energy
- Innovation
- Tech and data science

Link to our website: https://demo.vindhalur-example.is/
We are open to ideas.
Thank you!

Target Market(s)

Electricity consumers both homes and companies.

Number of Pages Required

1 page

Font styles to use
Serif
Sans Serif

```html
<!DOCTYPE html>
<html lang="is">
<head>
<meta charset="utf-8">
<title>Vindhalur</title>
<link rel="stylesheet" href="https://fonts.googleapis.com/css2?family=Cinzel:wght@400;700&family=Didact+Gothic&family=Mulish:wght@400&display=swap">
<style>
:root{
  --green:#849f00;
  --orange:#f55a00;
  --navy:#1d2a5b;
  --ink:#141414;
  --text:#222;
  --rule:#a9a8b0;
  --accent-red:#b0453a;
  --footer-ink:#3d4a08;
}
*{box-sizing:border-box;margin:0;padding:0}
html,body{width:1200px;height:1055px;overflow:hidden;background:#fff}
body{position:relative;font-family:'Mulish',sans-serif;color:var(--text)}
.hero{position:absolute;left:0;top:0;width:1200px;height:460px;
  background:
    linear-gradient(100deg,rgba(0,0,0,0) 55%,rgba(20,25,40,.35) 75%,rgba(40,40,30,.45) 100%),
    linear-gradient(180deg,#0a358a 0%,#2360b4 22%,#6e9fcf 40%,#e9dca0 62%,#f2c455 75%,#d58f1c 88%,#8a5410 100%);}
.hero-curve{position:absolute;left:0;top:0}
.brand{position:absolute;left:141px;top:32px;display:flex;align-items:center;gap:10px;
  font-family:'Cinzel',serif;font-weight:700;font-size:33px;color:#fff;letter-spacing:.5px}
.brand-dot{width:30px;height:30px;border-radius:50%;background:#fff}
.nav{position:absolute;right:142px;top:48px;display:flex;gap:26px;
  font-family:'Cinzel',serif;font-size:15px;color:#fff;letter-spacing:.4px}
.headline{position:absolute;left:144px;top:176px;font-family:'Cinzel',serif;font-weight:400;
  font-size:44px;line-height:55px;color:var(--ink);text-transform:uppercase}
.card{position:absolute;top:355px;width:295px;height:390px;background:#fff;
  border-bottom:3px solid var(--rule);box-shadow:0 0 2px rgba(0,0,0,.12);text-align:center}
.card-1{left:141px}.card-2{left:453px}.card-3{left:764px}
.icon-ring{position:absolute;left:87px;top:29px;width:122px;height:122px;border-radius:50%;
  border:1.5px dotted #999;display:flex;align-items:center;justify-content:center}
.card-title{position:absolute;left:0;right:0;top:166px;font-family:'Didact Gothic',sans-serif;font-weight:400;font-size:16px;color:#111}
.card-text{position:absolute;left:30px;right:30px;top:200px;font-size:12.2px;line-height:19px;color:#222}
.card-3 .card-text{left:38px;right:38px}
.btns{position:absolute;left:0;right:0;top:324px;display:flex;justify-content:center;gap:7px}
.btn{width:113px;height:38px;display:flex;align-items:center;justify-content:center;
  font-family:'Cinzel',serif;font-size:13.5px;color:#fff;letter-spacing:.6px;text-transform:uppercase}
.btn-green{background:var(--green)}.btn-orange{background:var(--orange)}
.prices{position:absolute;left:0;right:0;top:200px;display:flex}
.price{width:50%;text-align:center;font-size:12.2px;line-height:16px}
.price strong{display:block;font-family:'Didact Gothic',sans-serif;font-weight:400;font-size:20px;line-height:26px;margin-bottom:6px;color:#111}
.price-divider{position:absolute;left:146px;top:0;width:1px;height:78px;background:#ddd}
.compare{position:absolute;left:0;right:0;top:290px;font-size:12.2px}
.footer{position:absolute;left:0;top:817px;width:1200px;height:190px;background:var(--green)}
.contact{position:absolute;top:39px;display:flex;gap:14px}
.contact-email{left:141px}.contact-address{left:793px}
.contact-icon{width:43px;height:43px;border-radius:50%;background:var(--navy);border:1.5px solid #fff;
  display:flex;align-items:center;justify-content:center;margin-top:1px}
.contact-lines{font-size:14px;line-height:21px;color:var(--footer-ink)}
.contact-head{font-family:'Cinzel',serif;font-size:15px;letter-spacing:.8px;color:var(--footer-ink);line-height:20px}
.contact-lines.small{font-size:12.5px}
.company{position:absolute;left:0;right:0;top:134px;text-align:center;font-family:'Cinzel',serif;
  font-size:13px;line-height:19px;color:var(--footer-ink);letter-spacing:.3px}
.copyright{position:absolute;left:0;right:0;top:1020px;text-align:center;font-size:12.5px;color:#444}
</style>
</head>
<body>
<div class="hero" role="img" aria-label="Photograph of electricity pylons and power lines against a sunset sky"></div>
<svg class="hero-curve" width="1200" height="1055" viewBox="0 0 1200 1055" aria-hidden="true">
  <path d="M0 388 C 250 440 480 455 700 425 C 900 398 1080 395 1200 452 L1200 1055 L0 1055 Z" fill="#fff"/>
  <path d="M0 393 C 250 445 480 460 700 430 C 900 403 1080 400 1200 457" fill="none" stroke="var(--accent-red)" stroke-width="3"/>
</svg>

<div class="brand"><span class="brand-dot"></span>VINDHALUR</div>
<nav class="nav"><span>Viðskiptaskilmálar</span><span>Spurt &amp; svarað</span><span>Um Vindhalur</span></nav>

<h1 class="headline">Sama rafmagn<br>bara ódýrara!</h1>

<section class="card card-1">
  <div class="icon-ring">
    <svg width="44" height="62" viewBox="0 0 44 62" fill="none" stroke="var(--green)" stroke-width="3" stroke-linecap="round">
      <path d="M12 3v10M32 3v10M4 13h36v10a18 18 0 0 1-36 0z"/>
      <path d="M22 41v8a8 8 0 0 0 8 8"/>
      <path d="M24 20l-5 7h6l-4 7"/>
    </svg>
  </div>
  <h2 class="card-title">Velkomin Í Viðskipti</h2>
  <p class="card-text">Lorem ipsum dolor sit a consectetuer adipiscing elit, sed diam nonummy nibh euismod tincidunt ut laoreet dolore magna aliquam erat volutpat.Ut wisi enim ad minim veniam quis.</p>
  <div class="btns"><span class="btn btn-green">Fyrirtæki</span><span class="btn btn-orange">Heimili</span></div>
</section>

<section class="card card-2">
  <div class="icon-ring">
    <svg width="50" height="62" viewBox="0 0 50 62" fill="none" stroke="var(--green)" stroke-width="2.6">
      <path d="M2 2h36l10 10v48H2z"/><path d="M38 2v10h10"/>
      <path d="M12 13h8M30 13h-4M23 8v12" />
      <rect x="10" y="24" width="7" height="7"/><rect x="10" y="36" width="7" height="7"/><rect x="10" y="48" width="7" height="7"/>
      <path d="M22 27h18M22 39h18M22 51h18M22 32h14M22 44h14"/>
    </svg>
  </div>
  <h2 class="card-title">Verðskrá</h2>
  <div class="prices">
    <div class="price"><strong>6.95</strong>krónur / kWst</div>
    <div class="price"><strong>6.22</strong>krónur / kWst<br>rafmagnskynding</div>
    <span class="price-divider"></span>
  </div>
  <p class="compare">Gerðu verðsamanburð</p>
  <div class="btns"><span class="btn btn-green">Verðvaki</span></div>
</section>

<section class="card card-3">
  <div class="icon-ring">
    <svg width="46" height="76" viewBox="0 0 46 76" fill="none" stroke="var(--green)" stroke-width="4" stroke-linejoin="round">
      <path d="M30 3L4 44h18l-8 29 29-42H25z"/>
    </svg>
  </div>
  <h2 class="card-title">Framtíðin Er Spennandi</h2>
  <p class="card-text">Gerum raforkukerfið snallara saman. Vindhalur notar gervigreind, gagnavísindi og sjálfvirkni til að lágmarka kostnað og stuðla að okrujöfnuði</p>
  <div class="btns"><span class="btn btn-green">Vita meira</span></div>
</section>

<footer class="footer">
  <div class="contact contact-email">
    <span class="contact-icon">
      <svg width="24" height="20" viewBox="0 0 24 20" fill="none" stroke="#fff" stroke-width="1.6"><rect x="2" y="3" width="20" height="14" rx="1"/><path d="M2 4l10 7 10-7"/></svg>
    </span>
    <div class="contact-lines">vindhalur@vindhalur-example.is<br>555-0100</div>
  </div>
  <div class="contact contact-address">
    <span class="contact-icon">
      <svg width="16" height="22" viewBox="0 0 16 22" fill="none" stroke="#fff" stroke-width="1.6"><path d="M8 21s7-8 7-13A7 7 0 0 0 1 8c0 5 7 13 7 13z"/><circle cx="8" cy="8" r="2.5"/></svg>
    </span>
    <div>
      <div class="contact-head">HEIMILISFANG</div>
      <div class="contact-lines small">Dæmigötu 7 200 Kópavogi</div>
    </div>
  </div>
  <div class="company">Vindhalur ehf<br>Kennitala: 000000-0000 &nbsp; · &nbsp; Vskm Númer: 100000</div>
</footer>

<p class="copyright">Copyright © Vindhalur 2021 Allur Réttur Áskilin</p>
</body>
</html>
```